Equity, Effectiveness and Efficiency in charitable food relief sector

I am undertaking my PhD in food policy in the charitable food relief sector, specifically investigating the factors (supply, demand and capacity) that affect the introduction of nutrition policy and in turn, affect the sector's ability to achieve equity, effectiveness and efficiency.

I need a graphic device that incorporates this central idea of Equity, Effectiveness and Efficiency, and how the factors of supply, demand and capacity interact. There are sub-factors within supply (1-6), demand (7-10) and capacity (11 - 15). All these details are shown in the attached figure (Basic figure_Eq Effec Effic and factors.jpg)

This figure (Basic figure_Eq Effec Effic and factors.jpg) contains all the information I need in a graphic but I need something that is more visually appealing, and that can link the ideas in a format other than a table. The final graphic will outline how the food relief sector balances the core objectives of equity, effectiveness and efficiency with the factors (and sub-factors) of supply, demand and capacity.

```html
<!DOCTYPE html>
<html lang="en">
<head>
<meta charset="utf-8">
<title>Equity, Effectiveness, Efficiency: Supply, Demand, Capacity</title>
<link href="https://fonts.googleapis.com/css2?family=Montserrat:wght@400;500;600;700&display=swap" rel="stylesheet">
<style>
  :root{
    --green-top:#a9cf38;
    --green-bottom:#5fb546;
    --orange-top:#fdc71c;
    --orange-bottom:#f29a26;
    --blue-top:#55b9ea;
    --blue-bottom:#1a72ba;
    --blue-icon-bg:#50b4e7;
    --navy:#1f2b5b;
    --ring-grey:#ededee;
    --white:#ffffff;
    --c-orange:#f26b2a;
    --c-green:#129b48;
    --c-red:#d1232a;
    --c-yellow:#fdcb0b;
    --c-blue:#2a83c6;
    --c-purple:#5b2f83;
    --food-warm:#e07a4f;
    --food-green:#8cb552;
    --food-tan:#d8b58a;
    --shelf:#c98e4f;
  }
  *{margin:0;padding:0;box-sizing:border-box}
  html,body{width:1200px;height:927px;overflow:hidden;background:var(--white)}
  .canvas{position:relative;width:1200px;height:927px;overflow:hidden;font-family:"Montserrat",Arial,sans-serif;color:var(--white)}
  .backdrop{position:absolute;inset:0}
  .factor-title{position:absolute;font-weight:600;letter-spacing:0.3px;line-height:1}
  .factor-title.supply{left:64px;top:162px;font-size:41px}
  .factor-title.demand{left:496px;top:454px;font-size:41px}
  .factor-title.capacity{left:891px;top:151px;font-size:44px}
  .factor-list{position:absolute;list-style:none;font-size:19px;font-weight:500;line-height:1}
  .factor-list li{position:relative;padding-left:23px;height:43px}
  .factor-list li::before{content:"";position:absolute;left:2px;top:6px;width:7px;height:7px;border-radius:50%;background:var(--white)}
  .factor-list li.strong{font-weight:700}
  .factor-list li.semi{font-weight:600}
  .factor-list li.has-sub{height:30px}
  .factor-list li.sub{height:30px;font-weight:400}
  .factor-list li.sub::before{display:none}
  .factor-list li.sub.semi{font-weight:600}
  .factor-list li.sub span::before{content:"→ ";font-weight:400}
  .factor-list li.last-sub{height:43px}
  .list-supply{left:66px;top:230px}
  .list-demand{left:474px;top:531px}
  .list-capacity{left:893px;top:215px}
</style>
</head>
<body>
<div class="canvas">
  <svg class="backdrop" width="1200" height="927" viewBox="0 0 1200 927">
    <defs>
      <clipPath id="fan-clip"><circle cx="600" cy="-235" r="980"/></clipPath>
      <linearGradient id="grad-green" x1="0" y1="0" x2="0" y2="1">
        <stop offset="0" stop-color="var(--green-top)"/><stop offset="1" stop-color="var(--green-bottom)"/>
      </linearGradient>
      <linearGradient id="grad-orange" x1="0" y1="0" x2="0" y2="1">
        <stop offset="0.3" stop-color="var(--orange-top)"/><stop offset="1" stop-color="var(--orange-bottom)"/>
      </linearGradient>
      <linearGradient id="grad-blue" x1="0" y1="0" x2="1" y2="1">
        <stop offset="0" stop-color="var(--blue-top)"/><stop offset="1" stop-color="var(--blue-bottom)"/>
      </linearGradient>
      <linearGradient id="grad-food" x1="0" y1="0" x2="1" y2="0">
        <stop offset="0" stop-color="var(--food-green)"/>
        <stop offset="0.45" stop-color="var(--food-warm)"/>
        <stop offset="0.65" stop-color="var(--food-tan)"/>
        <stop offset="1" stop-color="var(--food-green)"/>
      </linearGradient>
      <linearGradient id="grad-emblem" x1="0" y1="0" x2="1" y2="0">
        <stop offset="0" stop-color="#f6d2bd"/>
        <stop offset="0.5" stop-color="#f7e6b0"/>
        <stop offset="1" stop-color="#cfd7ee"/>
      </linearGradient>
      <path id="motto-arc" d="M 362 0 A 238 238 0 0 0 838 0"/>
    </defs>

    <g clip-path="url(#fan-clip)" stroke="var(--white)" stroke-width="3">
      <polygon class="wedge-supply" points="0,0 597,0 283,760 0,760" fill="url(#grad-green)"/>
      <polygon class="wedge-demand" points="597,0 283,760 928,760" fill="url(#grad-orange)"/>
      <polygon class="wedge-capacity" points="597,0 1200,0 1200,760 928,760" fill="url(#grad-blue)"/>
    </g>

    <g class="hub">
      <circle cx="600" cy="0" r="278" fill="var(--white)"/>
      <circle cx="600" cy="0" r="270" fill="var(--ring-grey)"/>
      <circle cx="600" cy="0" r="210" fill="var(--white)"/>
      <g fill="none" stroke-width="4">
        <path d="M 398 0 A 212 212 0 0 0 416 85" stroke="var(--c-orange)"/>
        <path d="M 416 85 A 212 212 0 0 0 490 181" stroke="var(--c-green)"/>
        <path d="M 490 181 A 212 212 0 0 0 600 212" stroke="var(--c-red)"/>
        <path d="M 600 212 A 212 212 0 0 0 710 181" stroke="var(--c-yellow)"/>
        <path d="M 710 181 A 212 212 0 0 0 784 85" stroke="var(--c-blue)"/>
        <path d="M 784 85 A 212 212 0 0 0 802 0" stroke="var(--c-purple)"/>
      </g>
      <rect class="emblem-placeholder" x="512" y="22" width="178" height="128" rx="10" fill="url(#grad-emblem)" role="img" aria-label="Central emblem of the framework in six bright colours"/>
      <text font-family="Montserrat, Arial, sans-serif" font-weight="700" font-size="31" fill="var(--navy)" letter-spacing="1">
        <textPath href="#motto-arc" startOffset="50%" text-anchor="middle">EQUITY, EFFECTIVENESS, EFFICIENCY</textPath>
      </text>
    </g>

    <g class="icon-supply" fill="none" stroke="var(--white)" stroke-width="3" stroke-linejoin="round">
      <path d="M70 82 L100 62 L140 62 L140 130 L70 130 Z"/>
      <path d="M70 82 L110 82 L140 62"/>
      <path d="M110 82 L110 110"/>
      <path d="M88 82 L88 100 L94 96 L100 100 L100 82"/>
      <circle cx="137" cy="126" r="20" fill="#9ccc3a"/>
      <path d="M137 115 L137 136 M129 128 L137 136 L145 128"/>
    </g>

    <g class="icon-demand" fill="none" stroke="var(--white)" stroke-width="3" stroke-linejoin="round">
      <path d="M550 373 L580 353 L630 353 L630 423 L550 423 Z"/>
      <path d="M550 373 L600 373 L630 353"/>
      <path d="M600 373 L600 400"/>
      <path d="M570 373 L570 391 L576 387 L582 391 L582 373"/>
      <circle cx="622" cy="418" r="20" fill="var(--orange-top)"/>
      <path d="M622 429 L622 408 M614 416 L622 408 L630 416"/>
    </g>

    <g class="icon-capacity" stroke="var(--white)" stroke-width="3" stroke-linejoin="round" fill="var(--blue-icon-bg)">
      <g transform="translate(929 95)">
        <rect x="-6" y="-36" width="12" height="14" rx="2"/>
        <rect x="-6" y="-36" width="12" height="14" rx="2" transform="rotate(45)"/>
        <rect x="-6" y="-36" width="12" height="14" rx="2" transform="rotate(90)"/>
        <rect x="-6" y="-36" width="12" height="14" rx="2" transform="rotate(135)"/>
        <rect x="-6" y="-36" width="12" height="14" rx="2" transform="rotate(180)"/>
        <rect x="-6" y="-36" width="12" height="14" rx="2" transform="rotate(225)"/>
        <rect x="-6" y="-36" width="12" height="14" rx="2" transform="rotate(270)"/>
        <rect x="-6" y="-36" width="12" height="14" rx="2" transform="rotate(315)"/>
        <circle r="26"/>
        <circle r="12"/>
      </g>
      <g transform="translate(982 66)" stroke-width="2.5">
        <rect x="-3.5" y="-19" width="7" height="8" rx="1.5"/>
        <rect x="-3.5" y="-19" width="7" height="8" rx="1.5" transform="rotate(45)"/>
        <rect x="-3.5" y="-19" width="7" height="8" rx="1.5" transform="rotate(90)"/>
        <rect x="-3.5" y="-19" width="7" height="8" rx="1.5" transform="rotate(135)"/>
        <rect x="-3.5" y="-19" width="7" height="8" rx="1.5" transform="rotate(180)"/>
        <rect x="-3.5" y="-19" width="7" height="8" rx="1.5" transform="rotate(225)"/>
        <rect x="-3.5" y="-19" width="7" height="8" rx="1.5" transform="rotate(270)"/>
        <rect x="-3.5" y="-19" width="7" height="8" rx="1.5" transform="rotate(315)"/>
        <circle r="13"/>
        <circle r="6"/>
      </g>
    </g>

    <path class="food-placeholder" d="M0 800 C60 780 140 760 220 740 C300 730 380 760 460 765 C540 770 600 750 680 748 C760 746 820 775 900 765 C980 755 1060 760 1120 735 C1150 728 1180 740 1200 760 L1200 885 L0 885 Z" fill="url(#grad-food)" role="img" aria-label="Illustration of a row of foods on a shelf: vegetables, fruit, grains, cereal, bread, fish, eggs, dairy and oil"/>
    <rect class="shelf" x="0" y="880" width="1200" height="47" fill="var(--shelf)"/>
  </svg>

  <h2 class="factor-title supply">SUPPLY</h2>
  <ul class="factor-list list-supply">
    <li>Uncertain material supply</li>
    <li>Uncertain monetary supply</li>
    <li>Limited food supply</li>
    <li>Perishability</li>
    <li>Donor constraints</li>
    <li class="strong">Donor relationships</li>
  </ul>

  <h2 class="factor-title demand">DEMAND</h2>
  <ul class="factor-list list-demand">
    <li>Uncertain demand</li>
    <li>Limited demand visibility</li>
    <li class="strong">Client choice</li>
    <li>Food wastage</li>
  </ul>

  <h2 class="factor-title capacity">CAPACITY</h2>
  <ul class="factor-list list-capacity">
    <li class="has-sub">Storage</li>
    <li class="sub"><span>Cold</span></li>
    <li class="sub last-sub"><span>Warehouse</span></li>
    <li>Transportation</li>
    <li class="has-sub">Workspace</li>
    <li class="sub"><span>Volunteers</span></li>
    <li class="sub semi"><span>Expertise and training</span></li>
    <li class="sub semi"><span>Attitudes and Beliefs</span></li>
    <li class="sub semi"><span>Collaboration</span></li>
    <li class="sub semi last-sub"><span>Executive Support</span></li>
    <li class="semi">External stakeholders</li>
    <li>Budget</li>
  </ul>
</div>
</body>
</html>
```